Website Homepage Design for New Cosmetic Line

Design the Homepage for the website based on a provided Wireframe. Assets have been be provided for the design, with the expectation that the designer will provide the creative flair. Along with the homepage design, a list of site fonts and colours will also be needed for internal pages (but no internal page designs required. )
Layout/wireframe is here: http://verano-plumcosmetics.com/layout/ (and also attached in files as PNG and PDF)
No need to follow the Layout exactly as far as spacing and font go, just make sure all elements are on the page, and look amazing!
My Client gave these sites for comparable in the industry:
https://www.quorvabeauty.com/
https://www.marisoltenderwoodglow.com/ (does not like video in header though)

Moving Down the Wireframe:
Header Logo - Use the Text only from the logo, not the Circle at the top here
Navigation - Copy these items
Hero Image: Use the image stated. Feel free to add some creativity over it, make sure that the lips and product are still visible, and also that the Text that is being overlaid can be easily read
Arm Swatch and Lip Swatches, make them pop!
Featured Products, 2 of the images are in RAW from the photographer - you may want to convert them to jpg. Feel free to adjust if needed, for sizing and brightness. If you want to crop the images from the backgrounds, you could do that too to allow for more consistency.
Reviews show the needed content as well.

Footer speaks for itself - use the Full Round Logo here.

All Assets are here: https://files.stashbarn.net/folders/8kQwLmZ2xR4tYp9VnHc3JdE6sUb7aGo?usp=sharing

The main assets are also attached in a zip file, but there are more in the above shared link for additional creativity/resources

• Unique and Beautiful Design
Clear Layout
Follow Best Practices in Design layout for development (eg based on 12 grid)
Please Use Google Fonts

```html
<!DOCTYPE html>
<html lang="en">
<head>
<meta charset="utf-8">
<title>Verano-Plum Cosmetics</title>
<link rel="stylesheet" href="https://fonts.googleapis.com/css2?family=Jost:wght@300;400;500;600&family=Montserrat:wght@700;800&family=Barlow+Condensed:ital,wght@1,700&display=swap">
<style>
:root{
  --ink:#000;
  --crimson:#d41f4e;
  --rose:#c4507a;
  --paper:#fff;
  --mist:#f3f3f3;
  --blush:#f5ebe8;
  --gold:#f2c230;
  --text:#222;
}
*{box-sizing:border-box;margin:0;padding:0}
html,body{width:1200px;height:2841px;overflow:hidden}
body{position:relative;background:var(--paper);font-family:"Jost",sans-serif;color:var(--text)}
.abs{position:absolute}
.display{font-family:"Barlow Condensed",sans-serif;font-style:italic;font-weight:700;text-transform:uppercase}

/* header */
.site-header{position:absolute;left:0;top:0;width:1200px;height:108px;background:var(--ink)}
.brand{position:absolute;left:0;width:1200px;top:16px;text-align:center;color:#ddd;font-weight:300;font-size:34px;letter-spacing:.5px}
.header-rule{position:absolute;left:289px;top:64px;width:622px;height:1px;background:#7a1a33}
.nav a{position:absolute;top:79px;color:#fff;font-size:11px;letter-spacing:.6px;text-decoration:none;font-weight:400}
.header-icons{position:absolute;left:929px;top:80px}

/* hero */
.hero{position:absolute;left:0;top:108px;width:1200px;height:585px;background:radial-gradient(ellipse at 52% 30%,#b87a8e 0%,#8a5560 28%,#4b3532 55%,#5e5a5c 100%)}
.hero-title{position:absolute;left:226px;top:252px;padding-left:14px;border-left:5px solid var(--crimson);color:#fff;font-family:"Montserrat",sans-serif;font-weight:800;font-size:44px;letter-spacing:3px;line-height:1.05}
.hero-offer{position:absolute;left:226px;top:308px;color:#fff;font-size:32px;letter-spacing:.5px}
.hero-offer small{font-size:22px}
.hero-copy{position:absolute;left:228px;top:366px;width:460px;color:#fff;font-family:"Montserrat",sans-serif;font-weight:700;font-size:14px;line-height:16px;letter-spacing:.8px}
.btn{position:absolute;display:flex;align-items:center;justify-content:center;background:var(--crimson);color:#fff;font-family:"Jost",sans-serif;text-transform:uppercase;letter-spacing:.3px;clip-path:polygon(0 0,100% 0,93% 100%,0 100%)}
.hero .btn{left:226px;top:328px;width:145px;height:46px;font-size:15px}

/* mission */
.mission{position:absolute;left:0;top:693px;width:1200px;height:796px;background:var(--mist)}
.mission-deco{position:absolute;inset:0;background:linear-gradient(90deg,rgba(200,190,190,.35),rgba(255,255,255,0) 18%,rgba(255,255,255,0) 82%,rgba(200,190,190,.35))}
.section-title{position:absolute;left:0;width:1200px;text-align:center;color:var(--crimson);font-family:"Montserrat",sans-serif;font-weight:800;font-size:28px;letter-spacing:1.5px}
.mission-copy{position:absolute;left:300px;top:78px;width:600px;text-align:center;font-size:12.5px;line-height:16.5px;letter-spacing:.6px;color:#333}
.offer-card{position:absolute;left:225px;top:171px;width:750px;height:568px;background:var(--paper);box-shadow:0 4px 14px rgba(0,0,0,.25)}
.promo{position:absolute;left:109px;top:49px;width:533px;height:300px;border:2px solid var(--crimson);background:var(--rose);overflow:hidden}
.promo-photo{position:absolute;left:0;top:0;width:358px;height:296px;background:linear-gradient(180deg,#b38c80 0%,#c9a394 48%,#e2c2b8 52%,#d8b4a6 100%);clip-path:polygon(0 0,100% 0,76% 50%,100% 100%,0 100%)}
.promo-kicker{position:absolute;left:348px;top:62px;color:#fff;font-family:"Montserrat",sans-serif;font-weight:700;font-size:11px;letter-spacing:2px}
.promo-big{position:absolute;left:348px;top:82px;color:#fff;font-size:36px}
.promo-name{position:absolute;left:348px;top:130px;color:#fff;font-size:24px;line-height:32px;letter-spacing:.5px}
.promo .btn{left:348px;top:207px;width:100px;height:38px;font-size:11px}
.thumb{position:absolute;width:150px;height:151px;border:2px solid var(--crimson);background:linear-gradient(135deg,#7c3b3f,#e0566b 40%,#f08a8c 60%,#5a3434)}
.thumb.sale{border:none;box-shadow:0 3px 8px rgba(0,0,0,.35);background:linear-gradient(135deg,#3a2a2c,#a24a55 50%,#2c2022)}
.sale-panel{position:absolute;left:15px;top:15px;width:120px;height:121px;background:rgba(60,60,60,.75);border:1px solid rgba(255,255,255,.4);text-align:center;color:#fff}
.sale-panel b{display:block;margin-top:20px;font-family:"Montserrat",sans-serif;font-size:11px;letter-spacing:2px}
.sale-panel span{display:block;font-size:24px;margin-top:4px}

/* featured */
.featured{position:absolute;left:0;top:1489px;width:1200px;height:566px;background:var(--ink)}
.product{position:absolute;top:131px;width:237px;height:371px}
.product-photo{position:absolute;left:0;top:0;width:237px;height:289px;background:linear-gradient(180deg,#e9e9e9,#d4d4d4)}
.product-tab{position:absolute;right:0;top:289px;width:90px;height:82px;background:var(--crimson)}
.product-name{position:absolute;left:0;top:308px;color:#fff;font-size:19px;line-height:26px;letter-spacing:.3px}
.product .btn{left:125px;top:312px;width:100px;height:38px;font-size:11px;box-shadow:2px 2px 4px rgba(0,0,0,.3)}

/* reviews */
.reviews{position:absolute;left:0;top:2055px;width:1200px;height:456px;background:var(--paper)}
.dot{position:absolute;width:11px;height:11px;border-radius:50%;opacity:.35}
.review{position:absolute;top:88px;width:109px}
.avatar{width:109px;height:108px;background:linear-gradient(160deg,#d9b9a6,#8f6a58)}
.review h4{margin-top:11px;text-align:center;color:var(--crimson);font-size:11px;font-weight:600}
.stars{text-align:center;color:var(--gold);font-size:11px;letter-spacing:3px;line-height:14px}
.review p{margin-top:8px;font-size:8.4px;line-height:13px;text-align:justify;color:#333}

/* newsletter + footer */
.signup{position:absolute;left:0;top:2511px;width:1200px;height:330px;background:var(--blush)}
.signup-deco{position:absolute;left:0;top:0;width:560px;height:330px;background:radial-gradient(ellipse at 30% 55%,rgba(200,170,160,.35),rgba(245,235,232,0) 65%)}
.signup-label{position:absolute;left:244px;top:113px;font-size:16px;color:#111}
.signup-field{position:absolute;left:539px;top:106px;width:294px;height:38px;background:#fff;border:1px solid var(--rose)}
.signup-submit{position:absolute;left:856px;top:104px;width:100px;height:39px;background:var(--crimson);color:#fff;font-size:12px;display:flex;align-items:center;justify-content:center}
.site-footer{position:absolute;left:244px;top:179px;width:712px;height:107px;border:2px solid var(--crimson)}
.footer-links{position:absolute;left:28px;top:14px;font-size:13px;line-height:17.5px;color:#111}
.copyright{position:absolute;left:28px;top:82px;font-size:8.5px;color:#111}
.seal{position:absolute;left:311px;top:8px;width:88px;height:88px;border-radius:50%;border:2px solid #bbb;background:#fff;display:flex;align-items:center;justify-content:center;font-size:8px;font-weight:300;color:#777;text-align:center}
.footer-note{position:absolute;right:26px;top:14px;text-align:right;font-size:13px;line-height:17px;color:#111}
.social{position:absolute;top:60px;width:26px;height:26px;border-radius:50%;border:2px solid var(--crimson)}
</style>
</head>
<body>

<header class="site-header">
  <div class="brand">Verano-Plum Cosmetics</div>
  <div class="header-rule"></div>
  <nav class="nav">
    <a style="left:407px">Products</a>
    <a style="left:485px">About Us</a>
    <a style="left:568px">How To's</a>
    <a style="left:650px">Blog</a>
    <a style="left:709px">Connect With Us</a>
  </nav>
  <svg class="header-icons" width="48" height="14" viewBox="0 0 48 14">
    <circle cx="5" cy="5" r="3.2" fill="none" stroke="#fff" stroke-width="1.3"/><line x1="7.3" y1="7.3" x2="10" y2="10" stroke="#fff" stroke-width="1.4"/>
    <circle cx="24" cy="4" r="2.3" fill="#fff"/><path d="M20 11 q4 -6 8 0z" fill="#fff"/>
    <rect x="37" y="5" width="8" height="7" fill="#fff"/><path d="M39 5 v-2 a2 2 0 0 1 4 0 v2" fill="none" stroke="#fff" stroke-width="1"/>
  </svg>
</header>

<section class="hero" role="img" aria-label="Close-up photo of a model's pink lips holding a pink liquid lipstick tube">
  <h1 class="hero-title" style="top:144px">Verano-Plum Cosmetics</h1>
  <div class="hero-offer display" style="top:200px">$10 <small>with any</small> $25+ <small>purchase</small></div>
  <p class="hero-copy" style="top:258px">Lorem ipsum dolor sit amet, consectetur adipisicing elit, sed do eiusmod tempor incididunt ut labore et dolore magna aliqua.</p>
  <a class="btn">Shop Now</a>
</section>

<section class="mission">
  <div class="mission-deco" role="img" aria-label="Faint background of makeup brushes and cosmetic palettes"></div>
  <h2 class="section-title" style="top:34px">Our Mission</h2>
  <p class="mission-copy">Lorem ipsum dolor sit amet, consectetur adipisicing elit, sed do eiusmod tempor incididunt ut labore et dolore magna aliqua. Ut enim ad minim veniam, quis nostrud exercitation ullamco laboris nisi ut aliquip ex ea commodo consequat.</p>

  <div class="offer-card">
    <div class="promo">
      <div class="promo-photo" role="img" aria-label="Lip gloss swatches in plum, red, pink and berry on skin"></div>
      <div class="promo-kicker">ADDITIONAL</div>
      <div class="promo-big display">20% Off</div>
      <div class="promo-name display">Mini Lip Gloss<br>Set</div>
      <a class="btn">Shop Now</a>
    </div>
    <div class="thumb" style="left:106px;top:375px" role="img" aria-label="Grid of lip palette swatches"></div>
    <div class="thumb sale" style="left:298px;top:382px" role="img" aria-label="Collage of lip products">
      <div class="sale-panel"><b>SALE ITEMS</b><span class="display">15% Off</span>
        <svg width="20" height="20" viewBox="0 0 20 20" style="margin-top:6px"><circle cx="10" cy="10" r="10" fill="var(--crimson)"/><path d="M8 6 l4 4 -4 4" fill="none" stroke="#fff" stroke-width="1.6"/></svg>
      </div>
    </div>
    <div class="thumb" style="left:493px;top:380px" role="img" aria-label="Grid of lip colour swatches and lip palettes"></div>
  </div>
</section>

<section class="featured">
  <h2 class="section-title" style="top:38px;letter-spacing:3px">Featured Products</h2>
  <div class="product" style="left:225px">
    <div class="product-photo" role="img" aria-label="Red liquid lipstick tube"></div>
    <div class="product-tab"></div>
    <div class="product-name display">Liquid<br>Lipstick</div>
    <a class="btn">Shop Now</a>
  </div>
  <div class="product" style="left:481px">
    <div class="product-photo" role="img" aria-label="Open warm lip palette with six shades"></div>
    <div class="product-tab"></div>
    <div class="product-name display">Warm Lip<br>Palette</div>
    <a class="btn">Shop Now</a>
  </div>
  <div class="product" style="left:737px">
    <div class="product-photo" role="img" aria-label="Open sunset eye shadow palette with fifteen shades"></div>
    <div class="product-tab"></div>
    <div class="product-name display">Eye Shadow<br>Sunset Palette</div>
    <a class="btn">Shop Now</a>
  </div>
</section>

<section class="reviews">
  <span class="dot" style="left:58px;top:37px;background:#e9a35a"></span>
  <span class="dot" style="left:97px;top:11px;background:#9bc76b"></span>
  <span class="dot" style="left:113px;top:79px;background:#6d8fc9"></span>
  <span class="dot" style="left:346px;top:37px;background:#e9a35a"></span>
  <span class="dot" style="left:1078px;top:47px;background:#e9a35a"></span>
  <span class="dot" style="left:1114px;top:21px;background:#9bc76b"></span>
  <span class="dot" style="left:1130px;top:82px;background:#6d8fc9"></span>
  <span class="dot" style="left:1080px;top:200px;background:#9bc76b"></span>
  <span class="dot" style="left:1046px;top:230px;background:#e9a35a"></span>
  <span class="dot" style="left:97px;top:367px;background:#9bc76b"></span>
  <span class="dot" style="left:58px;top:398px;background:#e9a35a"></span>
  <span class="dot" style="left:113px;top:432px;background:#6d8fc9"></span>
  <span class="dot" style="left:780px;top:310px;background:#e9a35a"></span>
  <span class="dot" style="left:832px;top:368px;background:#6d8fc9"></span>
  <h2 class="section-title" style="top:30px;letter-spacing:2px">REVIEW</h2>

  <div class="review" style="left:225px"><div class="avatar" role="img" aria-label="Customer portrait"></div><h4>Lip Gloss</h4><div class="stars">★★★★★</div><p>Lorem ipsum dolor sit amet, consectetur adipisicing elit, sed do eiusmod tempor incididunt ut labore et dolore magna aliqua. Ut enim ad minim veniam, quis nostrud exercitation ullamco laboris nisi ut aliquip ex ea commodo consequat.</p></div>
  <div class="review" style="left:353px"><div class="avatar" role="img" aria-label="Customer portrait"></div><h4>Lip Gloss</h4><div class="stars">★★★★★</div><p>sed do eiusmod tempor incididunt ut labore et dolore magna aliqua. Ut enim ad minim veniam, quis nostrud exercitation ullamco laboris nisi ut aliquip ex ea commodo consequat.</p></div>
  <div class="review" style="left:481px"><div class="avatar" role="img" aria-label="Customer portrait"></div><h4>Lip Gloss</h4><div class="stars">★★★★★</div><p>sed do eiusmod tempor incididunt ut labore et dolore magna aliqua.</p></div>
  <div class="review" style="left:609px"><div class="avatar" role="img" aria-label="Customer eye makeup photos"></div><h4>Eye Shadow</h4><div class="stars">★★★★★</div><p>Lorem ipsum dolor sit amet, consectetur adipisicing elit, sed do eiusmod tempor incididunt ut labore et dolore magna aliqua. Ut enim ad minim veniam, quis nostrud exercitation ullamco laboris nisi ut aliquip ex ea commodo consequat.</p></div>
  <div class="review" style="left:737px"><div class="avatar" role="img" aria-label="Customer portrait"></div><h4>Lip Palette</h4><div class="stars">★★★★★</div><p>sed do eiusmod tempor incididunt ut labore et dolore magna aliqua. enim ad minim veniam, quis nostrud exercitation</p></div>
  <div class="review" style="left:866px"><div class="avatar" role="img" aria-label="Customer portrait"></div><h4>Lip Gloss</h4><div class="stars">★★★★★</div><p>sed do eiusmod tempor incididunt ut labore et dolore magna aliqua. enim ad minim veniam, quis nostrud exercitation ullamco laboris nisi ut aliquip ex ea commodo</p></div>
</section>

<section class="signup">
  <div class="signup-deco" role="img" aria-label="Soft background of makeup brushes and powder"></div>
  <h2 class="section-title" style="top:40px;font-weight:700">All Canadian-All Inclusive</h2>
  <div class="signup-label">Subscribe to our Newsletter</div>
  <div class="signup-field"></div>
  <div class="signup-submit">Submit</div>

  <footer class="site-footer">
    <div class="footer-links">About VPC<br>Blog<br>Sitemap</div>
    <div class="copyright">@2020 Verano-Plum Cosmetics.All Rights Reserved</div>
    <div class="seal">Verano-Plum Cosmetics</div>
    <div class="footer-note">Verano-Plum Cosmetics is a Vegan ang<br>Cruelty-Free Brand</div>
    <span class="social" style="left:617px"></span>
    <span class="social" style="left:655px;border-color:#111"></span>
  </footer>
</section>

</body>
</html>
```